Varnok Development and Management Corp. Business Card

A logo design project has been started for our Calgary-Alberta, Canada based land development and project management company. Using this logo, a clean, sleek, professional business card is to be developed (for digital or print media) representing the principals of the company (community, sustainability, and harmony).
Updates

Project Deadline Extended
Reason: Logo design recently completed.

Adobe Illustrator Vector file uploaded. Thanks, Lew

Target Market(s)

Similar business development professionals and other engineering project management personnel involved in land developemtn. Also used to as as the brand and image with both private individuals (Landowners), public officials (policy makers), and investors (banks, venture capitalists).

Industry/Entity Type

Digital

Requirements
Must have
• Open to designers opinion. Based on logo. Must have logo, and space for employee name, title, address, website, office / cell numbers.
Should not have
• No Palm trees or tropical references. Company is based in Calgary, Alberta, Canada.

```html
<!DOCTYPE html>
<html lang="en">
<head>
<meta charset="utf-8">
<title>Varnok Development and Management Corp. Business Card</title>
<link rel="stylesheet" href="https://fonts.googleapis.com/css2?family=Source+Sans+3:wght@400;600&display=swap">
<style>
  :root {
    --backdrop: #5e4332;
    --card: #23272f;
    --accent: #a4c639;
    --text-grey: #a9adb4;
    --name-grey: #b2b6bd;
    --mark-grey: #8e939b;
  }
  * { margin: 0; padding: 0; box-sizing: border-box; }
  html, body { width: 1200px; height: 1000px; overflow: hidden; }
  body {
    position: relative;
    background: var(--backdrop);
    font-family: "Source Sans 3", "Myriad Pro", sans-serif;
  }
  .card {
    position: absolute;
    left: 265px;
    width: 665px;
    height: 397px;
    background: var(--card);
  }
  .card-front { top: 74px; }
  .card-back { top: 533px; }

  .brand { position: absolute; display: flex; align-items: center; color: var(--accent); font-weight: 600; }
  .brand-square { background: var(--mark-grey); flex: none; }
  .brand-text { display: flex; flex-direction: column; line-height: 1; }
  .brand-word { letter-spacing: 2px; }

  .card-front .brand { left: 85px; top: 150px; gap: 22px; }
  .card-front .brand-square { width: 90px; height: 90px; }
  .card-front .brand-word { font-size: 72px; }
  .card-front .brand-sub { font-size: 22px; margin-top: 8px; }

  .card-back .brand { right: 22px; top: 46px; gap: 14px; }
  .card-back .brand-square { width: 56px; height: 56px; }
  .card-back .brand-word { font-size: 44px; }
  .card-back .brand-sub { font-size: 14px; margin-top: 4px; }

  .person { position: absolute; left: 23px; top: 136px; }
  .person-name { color: var(--name-grey); font-size: 22px; font-weight: 600; letter-spacing: 0.5px; line-height: 1.1; }
  .person-title { color: var(--accent); font-size: 16px; line-height: 1.2; }

  .contact { position: absolute; left: 23px; list-style: none; color: var(--text-grey); font-size: 17px; line-height: 23px; }
  .contact li { display: flex; align-items: flex-start; gap: 6px; }
  .contact svg { width: 12px; height: 12px; margin-top: 5px; flex: none; fill: var(--accent); }
  .contact-address { top: 204px; }
  .contact-phones { top: 270px; }
  .contact-phones li { margin-bottom: 2px; }
  .contact-web { top: 334px; }

  .accent-bar { position: absolute; left: 0; bottom: 0; width: 235px; height: 14px; background: var(--accent); }
</style>
</head>
<body>
  <section class="card card-front">
    <div class="brand">
      <span class="brand-square"></span>
      <span class="brand-text">
        <span class="brand-word">VARNOK</span>
        <span class="brand-sub">Development and Management Corp.</span>
      </span>
    </div>
  </section>

  <section class="card card-back">
    <div class="brand">
      <span class="brand-square"></span>
      <span class="brand-text">
        <span class="brand-word">VARNOK</span>
        <span class="brand-sub">Development and Management Corp.</span>
      </span>
    </div>

    <div class="person">
      <p class="person-name">EVAN HOLLOWAY</p>
      <p class="person-title">Director</p>
    </div>

    <ul class="contact contact-address">
      <li>
        <svg viewBox="0 0 12 12" aria-hidden="true"><path d="M6 0a4 4 0 0 0-4 4c0 3 4 8 4 8s4-5 4-8a4 4 0 0 0-4-4zm0 5.6A1.6 1.6 0 1 1 6 2.4a1.6 1.6 0 0 1 0 3.2z"/></svg>
        <span>14 Carrow Lane<br>Ashby VIC 3800</span>
      </li>
    </ul>

    <ul class="contact contact-phones">
      <li>
        <svg viewBox="0 0 12 12" aria-hidden="true"><path d="M3 0h6a1 1 0 0 1 1 1v10a1 1 0 0 1-1 1H3a1 1 0 0 1-1-1V1a1 1 0 0 1 1-1zm0.8 1.5v8h4.4v-8z"/></svg>
        <span>+61 402 558 217</span>
      </li>
      <li>
        <svg viewBox="0 0 12 12" aria-hidden="true"><path d="M0 4c1-2 3-3 6-3s5 1 6 3l-2 1-1-2H3L2 5zM2 6h8l1 5H1zm4 1.2a1.6 1.6 0 1 0 0 3.2 1.6 1.6 0 0 0 0-3.2z"/></svg>
        <span>+61 3 9412 6093</span>
      </li>
    </ul>

    <ul class="contact contact-web">
      <li>
        <svg viewBox="0 0 12 12" aria-hidden="true"><path d="M6 0a6 6 0 1 0 0 12A6 6 0 0 0 6 0zm0 1c.6.6 1.1 1.7 1.3 3H4.7C4.9 2.7 5.4 1.6 6 1zM1.2 5h2.4v2H1.2a4.8 4.8 0 0 1 0-2zm3.5 0h2.6v2H4.7zm3.7 0h2.4a4.8 4.8 0 0 1 0 2H8.4zM4.7 8h2.6C7.1 9.3 6.6 10.4 6 11c-.6-.6-1.1-1.7-1.3-3z"/></svg>
        <span>www.varnok.com</span>
      </li>
    </ul>

    <div class="accent-bar"></div>
  </section>
</body>
</html>
```